Website and Mobile Devices design for food related application.

We need a design that is simple yet playful. The design should be food related if possible.
This design will be on the website and the mobile platform markets we intend application to be deployed too.
This application/website is called "Bitelora[.com]. Its a random restaurant picker for the indecisive users.
Updates
Hi all, I picked a design. Again lots of great designs were submitted but I picked one that was more in line with what I wanted.
Target Market(s)
young internet savvy users.
Industry/Entity Type
Restaurant
Look and feel
Each slider illustrates characteristics of the customer's brand and the style your logo design should communicate.

```html
<!DOCTYPE html>
<html lang="en">
<head>
<meta charset="utf-8">
<title>Bitelora – Random Restaurant Picker</title>
<link href="https://fonts.googleapis.com/css2?family=Oswald:wght@300;400&display=swap" rel="stylesheet">
<style>
  :root {
    --page-bg: #121212;
    --frame-dark: #2e2416;
    --gold: #c0851f;
    --gold-deep: #a46d14;
    --cream: #f8f2e8;
    --panel: #ece2d2;
    --navy: #1c1b22;
    --text-dark: #3b3530;
    --text-muted: #7b6a55;
    --link: #d9a133;
    --copyright: #b9ad9b;
  }
  * { box-sizing: border-box; margin: 0; padding: 0; }
  html, body { width: 1147px; height: 1200px; overflow: hidden; }
  body {
    position: relative;
    background: var(--page-bg);
    font-family: "Oswald", "Arial Narrow", sans-serif;
    font-weight: 300;
  }

  /* Header */
  .nav-frame {
    position: absolute;
    background: var(--frame-dark);
    border-radius: 10px;
  }
  .nav-frame--refresh { left: 151px; top: 56px; width: 189px; height: 84px; }
  .nav-frame--contact { left: 793px; top: 56px; width: 189px; height: 84px; }
  .nav-frame--logo { left: 372px; top: 68px; width: 390px; height: 140px; border-radius: 14px; }
  .nav-bridge {
    position: absolute; top: 86px; height: 24px; background: var(--frame-dark);
  }
  .nav-bridge--left { left: 336px; width: 40px; }
  .nav-bridge--right { left: 758px; width: 40px; }

  .nav-button {
    position: absolute;
    top: 63px; width: 170px; height: 70px;
    background: var(--gold);
    border-radius: 6px;
    display: flex; align-items: center; justify-content: center; gap: 8px;
    color: var(--cream);
    font-size: 30px;
    font-weight: 300;
    text-transform: uppercase;
    text-decoration: none;
  }
  .nav-button--refresh { left: 160px; }
  .nav-button--contact { left: 802px; }
  .nav-button svg { width: 38px; height: 38px; }

  .brand {
    position: absolute;
    left: 383px; top: 77px; width: 368px; height: 122px;
    background: var(--gold);
    border-radius: 12px;
    padding: 7px;
  }
  .brand-inner {
    width: 100%; height: 100%;
    background: var(--cream);
    border-radius: 9px;
    display: flex; align-items: center; justify-content: center; gap: 12px;
    color: var(--gold-deep);
    font-size: 44px;
    font-weight: 300;
    letter-spacing: 1px;
    text-transform: uppercase;
  }
  .brand-dot {
    width: 14px; height: 14px; border-radius: 50%; background: var(--gold-deep);
  }

  /* Main panel */
  .main-panel {
    position: absolute;
    left: 7px; top: 293px; width: 1131px; height: 766px;
    background: var(--panel);
    border-radius: 12px;
  }
  .welcome {
    position: absolute;
    left: 29px; top: 22px; width: 1068px; height: 96px;
    background: var(--navy);
    border-radius: 8px;
    text-align: center;
  }
  .welcome-title {
    margin-top: 10px;
    color: var(--cream);
    font-size: 31px;
    font-weight: 300;
    line-height: 1.3;
    text-transform: uppercase;
  }
  .welcome-text {
    margin-top: 2px;
    color: var(--gold);
    font-size: 20px;
    font-weight: 300;
  }

  .restaurant-card {
    position: absolute;
    width: 246px; height: 233px;
    background: var(--cream);
    border-radius: 8px;
    padding: 10px 9px;
  }
  .restaurant-card::after {
    content: "";
    position: absolute;
    left: 8px; right: 8px; bottom: -30px; height: 22px;
    background: radial-gradient(ellipse at center top, rgba(0,0,0,0.28), rgba(0,0,0,0) 70%);
  }
  .restaurant-photo { width: 228px; height: 153px; }
  .restaurant-name {
    margin-top: 6px;
    color: var(--text-dark);
    font-size: 21px;
    font-weight: 300;
    letter-spacing: -0.2px;
    line-height: 1.2;
    white-space: nowrap;
  }
  .restaurant-location {
    margin-left: 3px;
    color: var(--text-muted);
    font-family: Arial, Helvetica, sans-serif;
    font-size: 14px;
  }

  /* Footer */
  .social {
    position: absolute; top: 1078px; left: 0; width: 1147px;
    display: flex; justify-content: center; gap: 11px;
  }
  .social-dot {
    width: 32px; height: 32px; border-radius: 50%; background: var(--gold-deep);
  }
  .footer-rule {
    position: absolute; left: 10px; top: 1124px; width: 1127px;
    border-top: 1px dotted #6c5a3e;
  }
  .footer-links {
    position: absolute; top: 1134px; left: 0; width: 1147px;
    text-align: center;
    font-family: Arial, Helvetica, sans-serif;
    font-size: 14px;
    color: var(--link);
    text-transform: uppercase;
  }
  .footer-links a { color: var(--link); text-decoration: none; }
  .copyright {
    position: absolute; top: 1159px; left: 0; width: 1147px;
    text-align: center;
    font-family: Arial, Helvetica, sans-serif;
    font-size: 12px;
    color: var(--copyright);
  }
</style>
</head>
<body>
  <header>
    <div class="nav-frame nav-frame--refresh"></div>
    <div class="nav-frame nav-frame--contact"></div>
    <div class="nav-bridge nav-bridge--left"></div>
    <div class="nav-bridge nav-bridge--right"></div>
    <div class="nav-frame nav-frame--logo"></div>

    <a class="nav-button nav-button--refresh" href="#">
      <svg viewBox="0 0 40 40" fill="none" stroke="#f8f2e8" stroke-width="4" stroke-linecap="round">
        <path d="M8 18 A12 12 0 0 1 30 12"/>
        <path d="M32 22 A12 12 0 0 1 10 28"/>
        <path d="M31 4 L31 13 L22 13" stroke-linejoin="round"/>
        <path d="M9 36 L9 27 L18 27" stroke-linejoin="round"/>
      </svg>
      Refresh
    </a>

    <div class="brand">
      <div class="brand-inner">Bitelora<span class="brand-dot"></span></div>
    </div>

    <a class="nav-button nav-button--contact" href="#">
      <svg viewBox="0 0 40 40" fill="none" stroke="#f8f2e8" stroke-width="3">
        <circle cx="20" cy="20" r="17"/>
        <path d="M14 11 L17 11 L18.5 16 L16.5 18 Q18.5 22 22 23.5 L24 21.5 L29 23 L29 26 Q27 29 23 28 Q14 25 12 16 Q11.5 12 14 11 Z" fill="#f8f2e8" stroke="none"/>
      </svg>
      Contact
    </a>
  </header>

  <main class="main-panel">
    <section class="welcome">
      <h1 class="welcome-title">Welcome Guest!</h1>
      <p class="welcome-text">If you can’t find your desired restaurant in the list below simply click the refresh button to show new list of randomized restaurants for you.</p>
    </section>

    <article class="restaurant-card" style="left:28px; top:148px;">
      <div class="restaurant-photo" role="img" aria-label="Warm dining room with round white tables" style="background:linear-gradient(160deg,#e8dccb,#9a6a45 60%,#4a2e1f);"></div>
      <h2 class="restaurant-name">Cool Brown Good Cousine</h2>
      <p class="restaurant-location">location: 136 street, adelay NY</p>
    </article>
    <article class="restaurant-card" style="left:303px; top:148px;">
      <div class="restaurant-photo" role="img" aria-label="Restaurant interior with blue lit ceiling" style="background:linear-gradient(170deg,#c6763a,#3fa3c4 45%,#5a3a25);"></div>
      <h2 class="restaurant-name">Blue James Classic Restaurant</h2>
      <p class="restaurant-location">location: 136 street, adelay NY</p>
    </article>
    <article class="restaurant-card" style="left:579px; top:148px;">
      <div class="restaurant-photo" role="img" aria-label="Golden dining hall with orange booths" style="background:linear-gradient(175deg,#b88a2a,#6b4a1f 50%,#c45a2e);"></div>
      <h2 class="restaurant-name">Cirular Restuarant Las Vegas</h2>
      <p class="restaurant-location">location: 136 street, adelay NY</p>
    </article>
    <article class="restaurant-card" style="left:854px; top:148px;">
      <div class="restaurant-photo" role="img" aria-label="Dark dining room with set tables" style="background:linear-gradient(170deg,#2c2a26,#6c6356 50%,#e2ddd4);"></div>
      <h2 class="restaurant-name">Cirular Restuarant Las Vegas</h2>
      <p class="restaurant-location">location: 136 street, adelay NY</p>
    </article>

    <article class="restaurant-card" style="left:28px; top:453px;">
      <div class="restaurant-photo" role="img" aria-label="Red dining room with hanging lamps" style="background:linear-gradient(170deg,#d9a23a,#6a2a1c 50%,#3a1a14);"></div>
      <h2 class="restaurant-name">Cool Brown Good Cousine</h2>
      <p class="restaurant-location">location: 136 street, adelay NY</p>
    </article>
    <article class="restaurant-card" style="left:303px; top:453px;">
      <div class="restaurant-photo" role="img" aria-label="Lounge with blue lights and dark sofas" style="background:linear-gradient(170deg,#2a2a3a,#3a5ea8 40%,#1a1a1e);"></div>
      <h2 class="restaurant-name">Blue James Classic Restaurant</h2>
      <p class="restaurant-location">location: 136 street, adelay NY</p>
    </article>
    <article class="restaurant-card" style="left:579px; top:453px;">
      <div class="restaurant-photo" role="img" aria-label="Underwater restaurant in an aquarium tunnel" style="background:linear-gradient(175deg,#3a8fc4,#2a6a9a 55%,#1a3048);"></div>
      <h2 class="restaurant-name">Cirular Restuarant Las Vegas</h2>
      <p class="restaurant-location">location: 136 street, adelay NY</p>
    </article>
    <article class="restaurant-card" style="left:854px; top:453px;">
      <div class="restaurant-photo" role="img" aria-label="Bright dining room with arches and white tables" style="background:linear-gradient(170deg,#e8c89a,#f2ece2 50%,#8a5a3a);"></div>
      <h2 class="restaurant-name">Cirular Restuarant Las Vegas</h2>
      <p class="restaurant-location">location: 136 street, adelay NY</p>
    </article>
  </main>

  <footer>
    <nav class="social" aria-label="Social links">
      <span class="social-dot"></span>
      <span class="social-dot"></span>
      <span class="social-dot"></span>
      <span class="social-dot"></span>
      <span class="social-dot"></span>
    </nav>
    <div class="footer-rule"></div>
    <p class="footer-links"><a href="#">Home</a> &nbsp;·&nbsp; <a href="#">Contact Us</a></p>
    <p class="copyright">© Copyright 2013 Bitelora. All Rights Reserved</p>
  </footer>
</body>
</html>
```